Brusola Card Design Project

Our company,Brusola, is focusing B to B, and people receiving this card are managers or engineers in the handset maker in the world.
Therefore we hope this to be designed strictly serious one but it needs cool and unique style which could imagine something innovation from the card.

This card will be used for Japanese,Chinese and English.
Please consider 2 byte character usage.

It Company

```html
<!DOCTYPE html>
<html lang="en">
<head>
<meta charset="utf-8">
<title>Brusola Business Card</title>
<link rel="stylesheet" href="https://fonts.googleapis.com/css2?family=Josefin+Sans:wght@600;700&family=Open+Sans:wght@400&display=swap">
<style>
  :root {
    --backdrop: #7a1416;
    --card-white: #ffffff;
    --card-dark: #5a5a5a;
    --ink-grey: #6e6e6e;
    --ink-soft: #8a8a8a;
    --mark-grey: #8c8c8c;
    --rule: #c9c9c9;
    --web-ink: #d0d0d0;
  }
  * { margin: 0; padding: 0; box-sizing: border-box; }
  html, body { width: 1200px; height: 900px; overflow: hidden; }
  body {
    background: var(--backdrop);
    position: relative;
    font-family: "Open Sans", Arial, sans-serif;
  }
  .card {
    position: absolute;
    left: 330px;
    width: 604px;
    height: 392px;
    border-radius: 10px;
    overflow: hidden;
    box-shadow: 0 6px 18px rgba(0,0,0,0.35);
  }
  .card-front { top: 30px; background: var(--card-white); }
  .card-back { top: 468px; background: var(--card-dark); }

  .brand-mark {
    position: absolute;
    left: 258px;
    top: 56px;
    width: 96px;
    height: 96px;
    border-radius: 50%;
    background: var(--mark-grey);
  }
  .wordmark {
    position: absolute;
    top: 196px;
    left: 0;
    width: 100%;
    text-align: center;
    font-family: "Josefin Sans", Arial, sans-serif;
    font-weight: 700;
    font-size: 32px;
    letter-spacing: 1.5px;
    color: var(--ink-grey);
  }
  .divider {
    position: absolute;
    left: 304px;
    top: 280px;
    width: 1px;
    height: 112px;
    background: linear-gradient(to bottom, rgba(200,200,200,0), var(--rule) 30%, var(--rule));
  }
  .contact-list {
    position: absolute;
    right: 312px;
    top: 286px;
    list-style: none;
    text-align: right;
    font-size: 10px;
    line-height: 25px;
    color: var(--ink-soft);
  }
  .contact-icons {
    position: absolute;
    left: 316px;
    top: 292px;
    display: flex;
    flex-direction: column;
    gap: 12px;
  }
  .contact-icons svg { width: 13px; height: 13px; fill: var(--ink-soft); }
  .person {
    position: absolute;
    left: 354px;
    top: 316px;
    color: var(--ink-soft);
  }
  .person-name { font-size: 11px; letter-spacing: 0.5px; }
  .person-title { font-size: 9px; margin-top: 3px; }

  .back-art {
    position: absolute;
    inset: 0;
    background:
      radial-gradient(ellipse 420px 300px at 420px 140px, rgba(225,225,225,0.9), rgba(175,175,175,0.55) 50%, rgba(90,90,90,0) 85%),
      linear-gradient(135deg, #4a4a4a 0%, #5c5c5c 40%, #8a8a8a 100%);
  }
  .web-address {
    position: absolute;
    left: 40px;
    bottom: 24px;
    font-size: 24px;
    color: var(--web-ink);
    letter-spacing: 0.5px;
  }
</style>
</head>
<body>
  <section class="card card-front">
    <div class="brand-mark" aria-hidden="true"></div>
    <div class="wordmark">BRUSOLA</div>
    <div class="divider"></div>
    <ul class="contact-list">
      <li>555 204 317</li>
      <li>2140 Harbor Lane Fremont, CA 94500</li>
      <li>hello@brusolamail.com</li>
      <li>Linkline.com/Brusola</li>
    </ul>
    <div class="contact-icons">
      <svg viewBox="0 0 16 16" aria-label="phone"><rect x="2" y="3" width="12" height="3" rx="1.5"/><rect x="4" y="7" width="8" height="7" rx="1"/></svg>
      <svg viewBox="0 0 16 16" aria-label="address"><path d="M8 1a4.5 4.5 0 0 0-4.5 4.5C3.5 9 8 15 8 15s4.5-6 4.5-9.5A4.5 4.5 0 0 0 8 1zm0 6.3a1.8 1.8 0 1 1 0-3.6 1.8 1.8 0 0 1 0 3.6z"/></svg>
      <svg viewBox="0 0 16 16" aria-label="email"><path d="M1 4h14v9H1z M1 4l7 5 7-5" fill="none" stroke="#8a8a8a" stroke-width="1.5"/></svg>
      <svg viewBox="0 0 16 16" aria-label="web"><circle cx="8" cy="8" r="6"/></svg>
    </div>
    <div class="person">
      <div class="person-name">KEN ARATA</div>
      <div class="person-title">GRAPHIC DESIGNER</div>
    </div>
  </section>

  <section class="card card-back">
    <div class="back-art" role="img" aria-label="Large grey brand motif sweeping across the card"></div>
    <div class="web-address">www.brusolaweb.com</div>
  </section>
</body>
</html>
```